IT consulting company looking for a modern business design for a website and a new logo

We are the IT-consulting company VendiMark from Germany and need a new and modern business website and a new logo. We are specialized in output management. Our services include business analysis, outsourcing, development, training and project leading. We wish for a design with nature pictures (mountains, lakes, rivers, forests, etc.) for our company with the colors green and blue. If it is possible, a slow-mo video of a nature scene. The design should be responsive and the menu should change to a hamburger menu. The following are: • Services / Solutions 1. Output Management 2. Outsourcing 3. Development 4. Business Analyst 5. Training • Partners • Careers • About Us 1. Project A 2. Project B 3. Project C • Contact Notes for the following categories: For "Services / Solutions" we want to conclude some contents from all the sub-points and sub-points below. Additionally, we would like to see some sub-point under "Services / Solutions". For Output Management: "5 Benefits of Output Management Systems (OMS) - OMS Simplifies and Accelerates External Communication - Helps Reduce Communication Mistakes - Provides Customers With Fast and Secure Responses to your questions - Employees can focus on the essential as they can access prepared templates - Companies get complete transparency about their communication "The point" partner does not have sub-points. The content here is a quote and the logo from the company Brel. For now, just placeholders on this site. The next point wants to be "career" without sub-point and wants to contain some text. Carrer options wants to be listed here. Next point wants to be "About us", where we need sub-points which we do not know exactly at this moment, but they will contain text. By clicking directly on "About us" we want to include pictures and texts about 6 employees for which we only need placeholders at the moment. The last point wants to be "contact", where customers can send us messages. The main page should include a story about our company, which can be a placeholder for now. For reference, designs have a look at: https://brelvantix.de/ https://www.lumortika.com/ https://www.tpvrano.de/ We prefer WordPress designs, created with the plugin ELEMENTOR, so that we can easily edit the content by ourselves. The final design should look professional, competent and modern.

Target Market(s)

With our website, we want to reach the following target groups. <br> <br> <br> <br> <br> <br> <br> <br> <br> <br> <br> <br> <br> <br> <br> <br> <br> <br> <br> <br> <br> <br> <br> <br> <br> <br> <br> <br> <br> <br> <br> <br> <br> <br> <br> <br> <br> <br> <br> <br> <br> <br> <br> <br> <br> <br> <br> <br> <br>

Industry/Entity Type

Consulting

Logo Text

(optionally) VendiMark

Font styles to use
Sans Serif

Colors

Designer to choose colors to be used in the design.

Requirements
Must have
• 1. Outsourcing 3. Development 4. Business Analyst 5. Training • Partners • Careers • About Us 1. Project A 2. Project B 3. Project C • Contact The above-mentioned background picture with nature motifs (mountains, lakes, rivers, forests, etc.). WordPress design in primary colors blue and green.
Nice to have
• ELEMENTOR template. Effects for the background pictures. Counter of all successful projects for Output Management, Business Analyst and Training

```html
<!DOCTYPE html>
<html lang="en">
<head>
<meta charset="utf-8">
<title>VendiMark – Output Management Consulting</title>
<link rel="stylesheet" href="https://fonts.googleapis.com/css2?family=Poppins:wght@400;500;600&family=Open+Sans:ital,wght@0,400;0,600;0,700;1,400&family=Lato:wght@400&display=swap">
<style>
:root{
  --green:#4b9a1e;
  --green-dark:#3f8618;
  --ink:#1d1d1d;
  --text:#555;
  --light:#f3f3f3;
  --line:#cfcfcf;
  --inner:#dfe4da;
  --white:#fff;
}
*{box-sizing:border-box;margin:0;padding:0}
html,body{width:1200px;height:3749px;overflow:hidden}
body{position:relative;background:var(--white);font-family:"Open Sans",sans-serif;color:var(--text)}
.heading{font-family:"Poppins",sans-serif;font-weight:500;color:var(--ink);text-align:center}
section,header{position:absolute;left:0;width:1200px;overflow:hidden}
.abs{position:absolute}

/* Header + hero */
.hero{top:0;height:648px;background:#f6f5f2}
.hero-scene{position:absolute;inset:0;background:
  linear-gradient(180deg,
    #f8f8f7 0%,#f4f1ea 16%,#ece2cf 26%,#e3c9a0 33%,
    #8e93a3 38%,#3d4b6b 45%,#2c3a58 52%,#4e5f80 58%,
    #b9c3d2 64%,#e6eaf0 70%,#dfe4ec 78%,#c2ccdb 88%,#aab6c8 100%)}
.site-header{top:0;height:120px;background:transparent}
.brand{left:110px;top:40px;font-family:"Poppins",sans-serif;font-size:31px;font-weight:500;color:var(--ink)}
.nav{position:absolute;left:462px;top:50px;display:flex;align-items:center;font-family:"Poppins",sans-serif;font-size:15px;color:var(--ink)}
.nav a{color:inherit;text-decoration:none;margin-right:33px}
.nav a.active{color:var(--green)}
.nav .search{margin-right:28px}
.nav .lang{font-size:13px;color:#444}
.hero-title{top:142px;width:1200px;font-size:52px;font-weight:500}
.hero-sub{top:226px;width:1200px;text-align:center;font-family:"Lato",sans-serif;font-size:25px;color:#333}
.btn{display:flex;align-items:center;justify-content:center;background:var(--green);color:var(--white);font-family:"Open Sans",sans-serif;font-weight:700;border-radius:40px;text-transform:uppercase;text-decoration:none}
.hero-btn{left:505px;top:298px;width:190px;height:60px;font-size:18px}
.dots{left:562px;top:569px;display:flex;gap:6px}
.dots span{width:14px;height:14px;border-radius:50%;border:2px solid var(--white)}
.dots span.on{background:var(--white)}

/* Welcome */
.welcome{top:648px;height:800px}
.net-deco{background:radial-gradient(ellipse at center,rgba(120,190,80,.28),rgba(120,190,80,0) 70%)}
.net-deco.grey{background:radial-gradient(ellipse at center,rgba(150,150,150,.3),rgba(150,150,150,0) 70%)}
.welcome-title{top:160px;width:1200px;font-size:50px}
.welcome-text{top:254px;left:200px;width:800px;text-align:center;font-size:14.5px;line-height:30px;color:#555}
.video{left:368px;top:394px;width:466px;height:291px;background:linear-gradient(135deg,#e9ecee 0%,#cdd3d8 45%,#9aa2a8 70%,#dfe2e4 100%);box-shadow:0 8px 18px rgba(0,0,0,.22)}
.play{left:565px;top:506px}

/* Services */
.services{top:1448px;height:582px;background:var(--light)}
.services-title{top:72px;width:1200px;font-size:50px}
.service-label{font-family:"Poppins",sans-serif;font-size:21px;color:var(--ink);line-height:31px}
.service-center{top:414px;width:1200px;text-align:center;font-family:"Poppins",sans-serif;font-weight:600;font-size:58px;color:var(--green)}

/* Partners */
.partners{top:2030px;height:534px}
.partners-title{top:90px;width:1200px;font-size:50px}
.card{top:201px;width:310px;height:229px;border:1px solid var(--line);text-align:center;background:var(--white)}
.card-name{margin-top:40px;font-family:"Poppins",sans-serif;font-weight:600;font-size:34px;color:#2d3e7a;display:flex;align-items:center;justify-content:center;gap:10px}
.card-name i{display:inline-block;width:26px;height:26px;background:#2d3e7a}
.card-quote{margin:30px 14px 0;font-style:italic;font-size:13.5px;line-height:26px;color:#666}
.arrow{top:297px}

/* Career */
.career{top:2564px;height:474px;background:linear-gradient(90deg,#5aa530 0%,#4f9a27 55%,#5da833 100%)}
.career-title{left:110px;top:98px;font-family:"Poppins",sans-serif;font-weight:500;font-size:52px;color:var(--white)}
.career-text{left:110px;top:176px;width:400px;font-size:14.5px;line-height:29px;color:var(--white)}
.career-btn{left:110px;top:330px;width:143px;height:47px;background:var(--white);color:#222;font-size:14px}
.job{top:78px;width:242px;height:316px;background:var(--white)}
.job-photo{height:162px;background:linear-gradient(160deg,#d6dbe2 0%,#8b97a6 55%,#4a5566 100%)}
.job-photo.warm{background:linear-gradient(160deg,#6c7785 0%,#a48873 55%,#3d4450 100%)}
.job h3{margin:24px 0 0 20px;font-family:"Poppins",sans-serif;font-weight:500;font-size:17.5px;color:var(--ink)}
.job p{margin:12px 20px 0;font-size:13.5px;line-height:24px;color:#555}
.job .go{position:absolute;right:16px;bottom:-16px}

/* Contact */
.contact{top:3038px;height:711px;background:linear-gradient(180deg,#f7f7f6 0%,#f2f1ef 35%,#ece6e2 65%,#e4e1df 100%)}
.contact-title{top:110px;width:1200px;font-size:52px}
.col-title{top:228px;font-family:"Poppins",sans-serif;font-weight:400;font-size:21px;color:var(--ink)}
.field{border:1px solid #8a8a8a;border-radius:4px;background:rgba(255,255,255,.85);font-size:13px;color:#444;padding:12px 14px}
.submit{left:610px;top:510px;width:103px;height:42px;font-size:14px}
.info-row{left:778px;display:flex;align-items:flex-start;gap:15px;font-size:14px;line-height:24px;color:#444}
.info-row svg{flex:none}
.socials{left:776px;top:534px;display:flex;gap:14px}
.socials svg{display:block}
.footer-line{left:110px;top:604px;width:978px;height:1px;background:#bdbdbd}
.copyright{top:645px;width:1200px;text-align:center;font-size:13.5px;color:#555}
.to-top{left:1063px;top:644px}
</style>
</head>
<body>

<section class="hero">
  <div class="hero-scene" role="img" aria-label="Snow-capped mountain peaks lit by sunrise, rising above a sea of clouds"></div>
  <h1 class="heading abs hero-title">Specialised in Output Management</h1>
  <p class="abs hero-sub">We are a IT consulting company in Germany</p>
  <a class="btn abs hero-btn">Get a quote</a>
  <div class="abs dots"><span class="on"></span><span></span><span></span><span></span></div>
</section>

<header class="site-header">
  <div class="abs brand">VendiMark</div>
  <nav class="nav">
    <a class="active">Home</a><a>Services</a><a>Partner</a><a>Career</a><a>About us</a><a>Contact</a>
    <svg class="search" width="16" height="16" viewBox="0 0 16 16"><circle cx="6.5" cy="6.5" r="4.8" fill="none" stroke="#111" stroke-width="2.2"/><line x1="10" y1="10" x2="14.5" y2="14.5" stroke="#111" stroke-width="2.6" stroke-linecap="round"/></svg>
    <span class="lang">Eng <svg width="10" height="6" viewBox="0 0 10 6"><path d="M1 0h8L5 5z" fill="#333"/></svg></span>
  </nav>
</header>

<section class="welcome">
  <div class="abs net-deco" style="left:690px;top:0;width:510px;height:190px" role="img" aria-label="Green connected-nodes network decoration"></div>
  <div class="abs net-deco grey" style="left:0;top:600px;width:520px;height:200px" role="img" aria-label="Grey connected-nodes network decoration"></div>
  <h2 class="heading abs welcome-title">Welcome to VendiMark</h2>
  <p class="abs welcome-text">Nam libero tempore, cum soluta nobis est eligendi optio cumque nihil impedit quo minus id quod maxime pla ceat facere possimus, omnis voluptas assumenda est, omnis dolor repellendus. Temporibus autem quibusdam et aut officiis debitis aut rerum necessitatibus saepe eveniet ut et voluptates repudiand</p>
  <div class="abs video" role="img" aria-label="Video still: laptop with business charts on a desk next to a calculator"></div>
  <svg class="abs play" width="72" height="72" viewBox="0 0 72 72"><circle cx="36" cy="36" r="34" fill="#1b1b1b" stroke="var(--green)" stroke-width="3"/><path d="M29 23 L50 36 L29 49z" fill="#fff"/></svg>
</section>

<section class="services">
  <h2 class="heading abs services-title">Our Services</h2>
  <svg class="abs" style="left:0;top:0" width="1200" height="582" viewBox="0 0 1200 582">
    <circle cx="601" cy="582" r="255" fill="var(--inner)"/>
    <circle cx="601" cy="582" r="313" fill="none" stroke="var(--green)" stroke-width="2"/>
    <g fill="#fff" stroke="var(--green)" stroke-width="2">
      <circle cx="601" cy="269" r="44"/><circle cx="397" cy="346" r="44"/><circle cx="793" cy="346" r="44"/>
      <circle cx="320" cy="509" r="44"/><circle cx="877" cy="509" r="44"/>
    </g>
    <g fill="none" stroke="#111" stroke-width="2.6">
      <path d="M585 262a13 10 0 1 1 8 9l-8 4 2-6a10 8 0 0 1-2-7z"/>
      <path d="M603 268a11 8 0 1 1 8 13l5 4-8-2"/>
    </g>
    <circle cx="397" cy="346" r="15" fill="#111"/>
    <path d="M389 337c5 2 3 7 8 8s2 7 6 9M402 334c-2 4 4 5 7 8" stroke="#fff" stroke-width="2.5" fill="none"/>
    <g fill="#111"><rect x="778" y="333" width="3" height="25"/><rect x="778" y="356" width="30" height="3"/><rect x="784" y="344" width="4" height="11"/><rect x="791" y="338" width="4" height="17"/><rect x="798" y="341" width="4" height="14"/></g>
    <g fill="#111"><circle cx="320" cy="500" r="6"/><circle cx="308" cy="503" r="5"/><circle cx="332" cy="503" r="5"/><path d="M309 523a11 10 0 0 1 22 0z"/><path d="M298 519a9 8 0 0 1 12-6v6z"/><path d="M342 519a9 8 0 0 0-12-6v6z"/></g>
    <g fill="none" stroke="#111"><circle cx="870" cy="514" r="8" stroke-width="6" stroke-dasharray="3 2.3"/><circle cx="870" cy="514" r="3" stroke-width="2"/><circle cx="886" cy="500" r="5" stroke-width="4" stroke-dasharray="2 1.8"/><circle cx="887" cy="521" r="5" stroke-width="4" stroke-dasharray="2 1.8"/></g>
  </svg>
  <div class="abs service-label" style="left:0;width:1200px;text-align:center;top:170px">Training</div>
  <div class="abs service-label" style="right:878px;top:331px;text-align:right">Outsourcing</div>
  <div class="abs service-label" style="left:873px;top:314px">Business Analyst</div>
  <div class="abs service-label" style="right:950px;top:477px;text-align:right">Output<br>Management</div>
  <div class="abs service-label" style="left:948px;top:494px">Development</div>
  <div class="abs service-center">VendiMark</div>
</section>

<section class="partners">
  <h2 class="heading abs partners-title">Partners</h2>
  <svg class="abs arrow" style="left:44px" width="20" height="36" viewBox="0 0 20 36"><path d="M17 2 3 18l14 16" fill="none" stroke="#777" stroke-width="3"/></svg>
  <svg class="abs arrow" style="left:1136px" width="20" height="36" viewBox="0 0 20 36"><path d="M3 2l14 16L3 34" fill="none" stroke="#777" stroke-width="3"/></svg>
  <div class="abs card" style="left:112px"><div class="card-name"><i></i>Norvela</div><p class="card-quote">“ At vero eos et accusamus et iusto odio dignissimos ducimus qui blanditiis praesent ium voluptatum deleniti atque ”</p></div>
  <div class="abs card" style="left:445px"><div class="card-name" style="color:#6b2d84">Quintra</div><p class="card-quote">“ At vero eos et accusamus et iusto odio dignissimos ducimus qui blanditiis praesent ium voluptatum deleniti atque ”</p></div>
  <div class="abs card" style="left:778px"><div class="card-name" style="color:#1f5fb0">Halvexa</div><p class="card-quote">“ At vero eos et accusamus et iusto odio dignissimos ducimus qui blanditiis praesent ium voluptatum deleniti atque ”</p></div>
</section>

<section class="career" role="img" aria-label="Green-tinted photo of a team working in an office">
  <h2 class="abs career-title">Career</h2>
  <p class="abs career-text">Nam libero tempore, cum soluta nobis est eligendi optio cumque nihil impedit quo minus id quod maxime placeat facere possimus, omnis voluptas assumenda est, omnis dolor repellend ibus autem quibusda.</p>
  <a class="btn abs career-btn">View more</a>
  <article class="abs job" style="left:570px">
    <div class="job-photo" role="img" aria-label="Presenter addressing colleagues in a meeting room"></div>
    <h3>Finibus Bonoruet Malo</h3>
    <p>Nam libero tempore, cuisoluta nobis est eligendi optio cuque nihil impedit quo miq</p>
    <svg class="go" width="32" height="32" viewBox="0 0 32 32"><circle cx="16" cy="16" r="15" fill="#222" stroke="#fff" stroke-width="2"/><path d="M11 11l5 5-5 5M16 11l5 5-5 5" fill="none" stroke="#fff" stroke-width="2"/></svg>
  </article>
  <article class="abs job" style="left:847px">
    <div class="job-photo warm" role="img" aria-label="Colleagues collaborating around a laptop"></div>
    <h3>Finibus Bonoruet Malo</h3>
    <p>Nam libero tempore, cuisoluta nobis est eligendi optio cuque nihil impedit quo miq</p>
    <svg class="go" width="32" height="32" viewBox="0 0 32 32"><circle cx="16" cy="16" r="15" fill="#222" stroke="#fff" stroke-width="2"/><path d="M11 11l5 5-5 5M16 11l5 5-5 5" fill="none" stroke="#fff" stroke-width="2"/></svg>
  </article>
</section>

<section class="contact" role="img" aria-label="Faded city skyline with a television tower">
  <h2 class="heading abs contact-title">Contact Us</h2>
  <h3 class="abs col-title" style="left:110px">Contact form</h3>
  <div class="abs field" style="left:112px;top:284px;width:296px;height:45px">Name :</div>
  <div class="abs field" style="left:418px;top:284px;width:296px;height:45px">Phone no :</div>
  <div class="abs field" style="left:112px;top:346px;width:602px;height:44px">Email :</div>
  <div class="abs field" style="left:112px;top:408px;width:602px;height:83px">Message :</div>
  <a class="btn abs submit">Submit</a>

  <h3 class="abs col-title" style="left:778px">Contact Information</h3>
  <div class="abs info-row" style="top:282px">
    <svg width="34" height="34" viewBox="0 0 34 34"><circle cx="17" cy="17" r="16" fill="#fff" stroke="#bbb"/><path d="M17 9a5 5 0 0 1 5 5c0 4-5 10-5 10s-5-6-5-10a5 5 0 0 1 5-5z" fill="var(--green)"/><circle cx="17" cy="14" r="2" fill="#fff"/></svg>
    <span>4100 Lindenweg, Suite 12<br>Marbury, Florida 33020</span>
  </div>
  <div class="abs info-row" style="top:343px">
    <svg width="34" height="34" viewBox="0 0 34 34"><circle cx="17" cy="17" r="16" fill="#fff" stroke="#bbb"/><path d="M11 10l4-1 2 5-2 2c1 2 3 4 5 5l2-2 5 2-1 4c-8 0-15-7-15-15z" fill="var(--green)"/></svg>
    <span style="margin-top:5px">1 555 014 2277</span>
  </div>
  <div class="abs info-row" style="top:405px">
    <svg width="34" height="34" viewBox="0 0 34 34"><circle cx="17" cy="17" r="16" fill="#fff" stroke="#bbb"/><rect x="10" y="12" width="14" height="10" fill="var(--green)"/><path d="M10 12l7 6 7-6" fill="none" stroke="#fff" stroke-width="1.5"/></svg>
    <span style="margin-top:5px">info@vendimark.com</span>
  </div>
  <h3 class="abs col-title" style="left:778px;top:485px">Social Media</h3>
  <div class="abs socials">
    <svg width="34" height="34" viewBox="0 0 34 34" aria-label="Chat"><circle cx="17" cy="17" r="15.5" fill="#fff" stroke="var(--green)" stroke-width="2"/><path d="M10 12h14v8h-8l-4 3v-3h-2z" fill="var(--green)"/></svg>
    <svg width="34" height="34" viewBox="0 0 34 34" aria-label="Share link"><circle cx="17" cy="17" r="15.5" fill="#fff" stroke="var(--green)" stroke-width="2"/><circle cx="12" cy="17" r="2.6" fill="var(--green)"/><circle cx="22" cy="11.5" r="2.6" fill="var(--green)"/><circle cx="22" cy="22.5" r="2.6" fill="var(--green)"/><path d="M12 17l10-5.5M12 17l10 5.5" stroke="var(--green)" stroke-width="1.6"/></svg>
    <svg width="34" height="34" viewBox="0 0 34 34" aria-label="Website"><circle cx="17" cy="17" r="15.5" fill="#fff" stroke="var(--green)" stroke-width="2"/><circle cx="17" cy="17" r="7.5" fill="none" stroke="var(--green)" stroke-width="1.8"/><ellipse cx="17" cy="17" rx="3.2" ry="7.5" fill="none" stroke="var(--green)" stroke-width="1.5"/><path d="M9.5 17h15" stroke="var(--green)" stroke-width="1.5"/></svg>
  </div>

  <div class="abs footer-line"></div>
  <p class="abs copyright">Copyright © 2019, VendiMark. All rights reserved.</p>
  <svg class="abs to-top" width="30" height="18" viewBox="0 0 30 18"><path d="M2 16 15 3l13 13" fill="none" stroke="#9a9a9a" stroke-width="3"/></svg>
</section>

</body>
</html>
```